A Dedicated Thank You to my Dad

Proposed Dimensions: Approx. 20" x 30"

For Father's Day, I wrote a dedication to my Dad that encapsulates my gratitude for everything he does, and everything he is. His birthday is on August 3, but it is more important for me to transform this dedication into a meaningful and memorable gift than to meet any deadline. I would love an image that captures the relationship between a father and his son, accompanied by my words of thanks in some sort of font that is appropriate for the message (calligprahy? not sure about that).

I had actually posted the Thank You on Pixelmarrow as a public post, so anyone with an account can read it: https://www.pixelmarrow.example/photo.php?fbid=40872219360548813&set=a.318760942157.6650129.3908471&type=1&theater

Only the words starting with "Thank you ..." should be on the poster.

Target Market(s)

This is a personal gift for my Dad. He doesn't have the best of eyesight, so having the words in a really small font would not be particularly helpful. :-)

Requirements
Must have
• * Personable
* Warm
* Inviting
* Memorable
* Understated more favored over Loud
Should not have
• * An entire palette of colors
* Wacky colors or fonts

```html
<!DOCTYPE html>
<html lang="en">
<head>
<meta charset="utf-8">
<title>Thank You Dad</title>
<link rel="stylesheet" href="https://fonts.googleapis.com/css2?family=Anton&family=Dancing+Script:wght@700&display=swap">
<style>
  :root {
    --photo-light: #e6d2bd;
    --photo-mid: #c9a48c;
    --photo-deep: #7d6a66;
    --panel: #c9aa80;
    --divider: #f4ece2;
    --ink-light: #ffffff;
  }
  html, body {
    margin: 0;
    padding: 0;
    width: 693px;
    height: 1200px;
    overflow: hidden;
    background: var(--divider);
  }
  .poster {
    position: relative;
    width: 693px;
    height: 1200px;
    overflow: hidden;
  }
  .portrait {
    position: absolute;
    top: 0;
    left: 0;
    width: 693px;
    height: 528px;
    background:
      radial-gradient(ellipse 28% 45% at 32% 68%, rgba(90,80,82,0.55), transparent 70%),
      radial-gradient(ellipse 30% 50% at 60% 62%, rgba(70,70,90,0.55), transparent 70%),
      linear-gradient(180deg, var(--photo-light) 0%, var(--photo-mid) 70%, var(--photo-deep) 100%);
  }
  .portrait-wash {
    position: absolute;
    top: 0;
    left: 0;
    width: 693px;
    height: 130px;
    background: rgba(255, 255, 255, 0.18);
  }
  .headline {
    position: absolute;
    top: 28px;
    left: 0;
    width: 693px;
    margin: 0;
    text-align: center;
    font-family: "Anton", "Oswald", sans-serif;
    font-weight: 400;
    font-size: 46px;
    letter-spacing: 0.5px;
    color: var(--ink-light);
  }
  .dedication {
    position: absolute;
    top: 532px;
    left: 0;
    width: 693px;
    height: 668px;
    box-sizing: border-box;
    padding: 12px 14px 0;
    background: var(--panel);
    overflow: hidden;
  }
  .dedication-text {
    margin: 0;
    font-family: "Dancing Script", cursive;
    font-weight: 700;
    font-size: 16.5px;
    line-height: 18.4px;
    letter-spacing: 0.3px;
    word-spacing: 2px;
    text-align: justify;
    color: var(--ink-light);
  }
</style>
</head>
<body>
<main class="poster">
  <div class="portrait" role="img" aria-label="Photograph of a smiling son and his father standing arm in arm in a living room, a framed garden painting on the wall behind them"></div>
  <div class="portrait-wash"></div>
  <h1 class="headline">THANK YOU DAD.</h1>
  <section class="dedication">
    <p class="dedication-text">“Thank you Dad, for, after the initial shock, embracing the unexpected news that you were about to have twins. Thank you for buying enough diapers to single-handedly enable B &amp; K to make a profit. Thank you for always carrying us to the car after we fell asleep, even after we were definitely old enough to walk it. Thank you for not telling on us when we were only pretending to nap. Thank you for welcoming more people to stay with us than I can count. Thank you for sitting through more showings of "Slick Hair" and "Comet Raiders" than any human should endure. Thank you for doggedly trying to teach me that the beach is not to be feared nor cleaned. Thank you for working two jobs, for years, to make ends meet. Thank you for loading us all up in the station wagon, pillows in tow, so we could watch the first drive-in movie together and squint in the second. Thank you for, as coach, letting me take a fake rabbit's foot onto the soccer field. Thank you for being willing to put a hit out on my guitar teacher when he beat feet. Thank you for letting me sing in my room as if I were the originating artist. Thank you for making car trips with you, wherever we were going, fun and special. Thank you for proudly and patiently taking me to my first nerd conference in junior high. Thank you for putting up with the commutes you did, for decades, so we could grow up amongst family in an incredible community. Thank you for my dry sense of humour. I cherish it. Thank you for finding a way, by hook or by crook, to send three children to college at the same time, and to allow me to go to the college of my dreams. Thank you for never giving up on trying to convince me that imperfection is not a failure. Thank you for mispronouncing, I believe on purpose, pop culture references in a way that only you can. Thank you for teaching me to try to find the good in everyone. Thank you for waiting to laugh out loud with Mom until after the police left when my camp friends and I apparently made too much noise. Thank you for showing me that there is peace to be found in stillness and quiet. Thank you for demonstrating the fun that can be had and the truths that can be gleaned from philosophical and political debate. Thank you for accepting me for who I am, no matter who I love, and for helping me to accept myself. Thank you for doing whatever you can to help whoever you can, whether friend, family or stranger. Thank you for trusting me enough to let your guard sometimes to let me know how you are truly doing. Thank you for insisting, year after year, that time with you means more than any gift I could ever purchase. That is one lesson, amongst so many, that I will pass down to our next generation.” - Theo</p>
  </section>
</main>
</body>
</html>
```